Business Cards and Logo needed for Rum Website

I need a smart, modern but fun business card (and Logo) to help promote my website BrightBarrelNote.com

The website contains reviews of Rum (and eventually other spirits) as well as news and blog posts.

I would like a 2-sided design, with the logo and company name on one side and text on the other.

Text fields required are:
Name (Dan Wheeler)
Website (www.brightbarrelnote.com)
Email (dan@brightbarrelnote.com)
Twitter (@BrightBarrelNote)

For the logo i'm open to suggestions however it must incorporate a wooden Cask and a number of Stars. Ideas so far have been for a Cask surrounded in a number of Stars forming a circle around it with the text Bright Barrel Note underneath. The logo should be modern but also a little bit cartoony and stylised. General drink/spirits themes will also be considered.

Colours: I like the idea of yellow text with black background but again i'm open to suggestions on what would work well. Contrasting colours for the 2-sides would be good.

Cards will be printed via Printlo.com so please consult their style guidelines if required: http://uk.printlo.com/help/faq/templates-and-guidelines.html

Requirements
Must have
• A spirits Cask
A number of Stars (preferrably yellow or gold)

```html
<!DOCTYPE html>
<html lang="en">
<head>
<meta charset="utf-8">
<title>Bright Barrel Note – Business Cards</title>
<link rel="stylesheet" href="https://fonts.googleapis.com/css2?family=Jost:wght@400&display=swap">
<style>
  :root {
    --page-bg: #000000;
    --wood-dark-1: #6b6455;
    --wood-dark-2: #857b69;
    --wood-dark-3: #544d41;
    --wood-light-1: #ebe6da;
    --wood-light-2: #d6cfbe;
    --wood-light-3: #e2dccd;
    --plank-line: rgba(22, 18, 12, 0.75);
    --plank-gap: #2a2218;
    --badge-fill: rgba(38, 26, 14, 0.8);
    --badge-edge: rgba(20, 12, 6, 0.55);
    --star-yellow: #e8e25a;
    --ink-brown: #4a2c18;
  }
  html, body {
    margin: 0;
    padding: 0;
    width: 1200px;
    height: 900px;
    overflow: hidden;
    background: var(--page-bg);
    font-family: "Jost", "Futura", sans-serif;
  }
  .canvas {
    position: relative;
    width: 1200px;
    height: 900px;
  }
  .card {
    position: absolute;
    width: 589px;
    height: 386px;
    overflow: hidden;
    box-shadow: inset 0 0 0 2px rgba(255,255,255,0.15), inset 0 0 8px rgba(0,0,0,0.5);
  }
  .card--front-a { left: 7px;   top: 44px; }
  .card--front-b { left: 604px; top: 44px; }
  .card--back    { left: 305px; top: 469px; }

  .wood {
    position: absolute;
    inset: 0;
  }
  .wood--dark {
    background:
      repeating-linear-gradient(180deg,
        rgba(255,255,255,0.06) 0 6px, rgba(0,0,0,0.05) 6px 14px,
        rgba(255,255,255,0.03) 14px 22px, rgba(0,0,0,0.07) 22px 34px),
      linear-gradient(180deg, var(--wood-dark-2), var(--wood-dark-1) 45%, var(--wood-dark-3));
  }
  .wood--light {
    background:
      repeating-linear-gradient(180deg,
        rgba(0,0,0,0.03) 0 5px, rgba(255,255,255,0.05) 5px 13px, rgba(0,0,0,0.05) 13px 20px),
      linear-gradient(180deg, var(--wood-light-1), var(--wood-light-2) 50%, var(--wood-light-3));
  }
  .plank-line {
    position: absolute;
    left: 0;
    width: 100%;
    height: 3px;
    background: var(--plank-line);
  }
  .plank-joint {
    position: absolute;
    width: 2px;
    background: var(--plank-line);
  }
  .plank-gap {
    position: absolute;
    left: 0;
    width: 100%;
    height: 9px;
    background: var(--plank-gap);
  }

  .badge {
    position: absolute;
    border-radius: 50%;
    background: var(--badge-fill);
    box-shadow: 0 0 0 3px var(--badge-edge);
  }
  .badge--large { width: 268px; height: 268px; top: 59px; }
  .card--front-a .badge--large { left: 36px; }
  .card--front-b .badge--large { left: 162px; }
  .badge--small { width: 144px; height: 144px; left: 13px; top: 14px; }

  .brand-name {
    position: absolute;
    left: 0;
    right: 0;
    text-align: center;
    color: var(--star-yellow);
    font-weight: 400;
    letter-spacing: 1.5px;
    white-space: nowrap;
  }
  .badge--large .brand-name { top: 176px; font-size: 25px; }
  .badge--small .brand-name { top: 95px;  font-size: 13px; letter-spacing: 0.8px; }

  .contact {
    position: absolute;
    right: 9px;
    top: 230px;
    margin: 0;
    text-align: right;
    color: var(--ink-brown);
    font-size: 23px;
    letter-spacing: 1.6px;
    line-height: 38px;
  }
  .contact p { margin: 0; }
</style>
</head>
<body>
<main class="canvas">

  <section class="card card--front-a" aria-label="Card front, version one">
    <div class="wood wood--dark" role="img" aria-label="Weathered grey wooden deck planks"></div>
    <div class="plank-line" style="top:6px"></div>
    <div class="plank-line" style="top:73px"></div>
    <div class="plank-line" style="top:141px"></div>
    <div class="plank-line" style="top:212px"></div>
    <div class="plank-line" style="top:280px"></div>
    <div class="plank-line" style="top:348px"></div>
    <div class="plank-joint" style="left:373px; top:6px; height:67px"></div>
    <div class="plank-joint" style="left:185px; top:141px; height:71px"></div>
    <div class="plank-joint" style="left:580px; top:212px; height:68px"></div>
    <div class="plank-joint" style="left:380px; top:348px; height:38px"></div>
    <div class="badge badge--large">
      <span class="brand-name">Bright Barrel Note</span>
    </div>
  </section>

  <section class="card card--front-b" aria-label="Card front, version two">
    <div class="wood wood--dark" role="img" aria-label="Weathered grey wooden deck planks"></div>
    <div class="plank-line" style="top:6px"></div>
    <div class="plank-line" style="top:73px"></div>
    <div class="plank-line" style="top:141px"></div>
    <div class="plank-line" style="top:212px"></div>
    <div class="plank-line" style="top:280px"></div>
    <div class="plank-line" style="top:348px"></div>
    <div class="plank-joint" style="left:373px; top:6px; height:67px"></div>
    <div class="plank-joint" style="left:185px; top:141px; height:71px"></div>
    <div class="plank-joint" style="left:580px; top:212px; height:68px"></div>
    <div class="plank-joint" style="left:380px; top:348px; height:38px"></div>
    <div class="badge badge--large">
      <span class="brand-name">Bright Barrel Note</span>
    </div>
  </section>

  <section class="card card--back" aria-label="Card back">
    <div class="wood wood--light" role="img" aria-label="Pale bleached wooden planks"></div>
    <div class="plank-gap" style="top:31px"></div>
    <div class="plank-gap" style="top:212px"></div>
    <div class="badge badge--small">
      <span class="brand-name">Bright Barrel Note</span>
    </div>
    <div class="contact">
      <p class="contact__name">Dan Wheeler</p>
      <p class="contact__web">www.brightbarrelnote.com</p>
      <p class="contact__email">Email: dan@brightbarrelnote.com</p>
      <p class="contact__twitter">Twitter: @BrightBarrelNote</p>
    </div>
  </section>

</main>
</body>
</html>
```